Solar Business needs infographic for Act Now Campaign

A government solar rebate program is ending and I would like to send out an infographic in an email campaign.

I want to explain with text and graphics why people should ACT NOW! The material has been prepared in Word with Designer Notes at each step of the 7 step infographic. I'd like each step to flow into the next as best it can.

I've prepared the guide in green and would like the infographic in green or the colours of the logo, orange and reds. Key words are highlighted in red, don't need to be in red, just must stand out to the reader.

This is a 'call to action' infographic. Emphasis on ACT NOW with highlights on numbers. Keep the look and feel SIMPLE to highlight the URGENCY and the numbers % and $.

I added a photo of solar on a roof, as an optional extra. I've made a small change to the text/copy of the material in Word.

Deadline approaching. ACT NOW! People who are looking to save electricity costs and install solar

Reason: Deadline extended as additional material has been added and minor changes made to original text.

Target Market(s)

35-65
male and female
young couples, retired, working family

Industry/Entity Type

Government

Requirements
Must have
• CALL TO ACTION look and feel. Infographic not limited to one page, scrolling on like a webpage.

Would like to have only two colour themes. Green theme or Red and Orange theme to match the Brevora logo.
Nice to have
• Detailed in the brief.

Photo of solar provided as a stock image I own the rights to. Does not have to be used, included as an option.

```html
<!DOCTYPE html>
<html lang="en">
<head>
<meta charset="utf-8">
<title>Step 5 – Electricity prices are through the roof</title>
<link rel="stylesheet" href="https://fonts.googleapis.com/css2?family=Bebas+Neue&family=Rubik:wght@700&display=swap">
<style>
  :root {
    --leaf-bg: #cde4a6;
    --leaf-top: #d6eab5;
    --forest: #2f4a10;
    --rule: #5a6b2c;
    --alert-red: #e8262b;
    --photo-fill: #ffffff;
  }
  html, body {
    margin: 0;
    padding: 0;
    overflow: hidden;
  }
  .step-card {
    position: relative;
    width: 1200px;
    height: 986px;
    background: var(--leaf-bg);
    overflow: hidden;
  }
  .step-card__topband {
    position: absolute;
    left: 0; top: 0;
    width: 100%;
    height: 28px;
    background: var(--leaf-top);
    border-bottom: 4px solid var(--rule);
  }
  .step-header {
    margin: 0;
    font-weight: 400;
    font-family: "Bebas Neue", "Oswald", sans-serif;
    color: var(--forest);
  }
  .step-header__line {
    position: absolute;
    left: 38px;
    display: block;
    font-size: 82px;
    line-height: 82px;
    letter-spacing: 6px;
    white-space: nowrap;
  }
  .step-header__line--first {
    top: 101px;
  }
  .step-header__line--second {
    top: 192px;
  }
  .step-number {
    color: var(--alert-red);
    font-size: 133px;
    line-height: 0;
    letter-spacing: 0;
    margin-right: 14px;
  }
  .step-rule {
    position: absolute;
    left: 0;
    top: 274px;
    width: 100%;
    height: 4px;
    background: var(--rule);
  }
  .step-body {
    position: absolute;
    left: 34px;
    top: 305px;
    width: 385px;
    margin: 0;
    font-family: "Rubik", "Arial", sans-serif;
    font-weight: 700;
    font-size: 32px;
    line-height: 38.5px;
    letter-spacing: 1.1px;
    color: var(--forest);
    white-space: nowrap;
  }
  .step-photo {
    position: absolute;
    left: 423px;
    top: 302px;
    width: 735px;
    height: 552px;
    background: var(--photo-fill);
  }
</style>
</head>
<body>
  <main class="step-card">
    <div class="step-card__topband"></div>

    <h1 class="step-header">
      <span class="step-header__line step-header__line--first"><span class="step-number">5</span>Electricity prices are through</span>
      <span class="step-header__line step-header__line--second">the roof. Fix yours with Solar PV</span>
    </h1>

    <div class="step-rule"></div>

    <p class="step-body">
      Electricity prices<br>
      have doubled in the<br>
      last five years<br>
      and continue to<br>
      rise.&nbsp; Over 1 million<br>
      Australian homes<br>
      are saving on<br>
      electricity every day<br>
      with Solar PV.<br>
      Act now and start<br>
      paying less for<br>
      electricity now,<br>
      and for the next<br>
      25 years.
    </p>

    <div class="step-photo" role="img" aria-label="Photo of solar panels installed on a house roof"></div>
  </main>
</body>
</html>
```